Brand Business Card for Hotel Cloud Management System

Hello designers,
we are looking for a new brand business card for our product Roomvanta. Our brand Roomvanta is a hotel management system for small hotels, B&B, guesthouses etc. and just recently we are expanding our offer to other European markets. Therefore we need a business card that will communicate not only to the end-users (hoteliers) but also to potential business partners/ We would like the brand business card to be professional looking, but not too serius, modern, elegant, clean, Our brand color is orange, dark grey and it would be nice to see both combined.

Please visit our website www.roomvanta-example.eu to get more impression on what our brand roomvanta stands for.

Please find attached roomvanta logo.

Target Market(s)

small hotels, hoteliers, B&B owners, potential business partners

Industry/Entity Type

Software Service

Contact Information for Business Card

Roomvanta
- hotel software solutions - web booking engine - multi channel manager
www.roomvanta-example.eu
T: +38614007300
E: info@roomvanta-example.net

Font styles to use
Serif
Sans Serif

Colors
f37122
aaaaaa
606060
f6f6f6

Requirements
Must have
• Logo of the brand
• the layout of the business card should be in connection with the look and feel of the website roomvanta-example.eu and logo roomvanta;

```html
<!DOCTYPE html>
<html lang="en">
<head>
<meta charset="utf-8">
<title>Roomvanta business card</title>
<link rel="stylesheet" href="https://fonts.googleapis.com/css2?family=Fira+Sans:wght@500&family=Roboto:wght@400;700&display=swap">
<style>
  :root {
    --orange: #e9671c;
    --charcoal: #363a3e;
    --paper: #f4f4f4;
    --ink: #1c1c1c;
    --mute: #d6d6d6;
    --mute-dark: #4a4a4a;
    --backdrop: #bdbdbd;
  }
  * { box-sizing: border-box; margin: 0; padding: 0; }
  html, body { width: 1200px; height: 576px; overflow: hidden; }
  body {
    background: var(--backdrop);
    font-family: "Roboto", Arial, sans-serif;
    position: relative;
  }
  .card {
    position: absolute;
    top: 138px;
    width: 484px;
    height: 292px;
    border-radius: 13px;
    overflow: hidden;
  }
  .card-front { left: 82px; background: var(--charcoal); }
  .card-back { left: 600px; width: 482px; }
  .card-back .backdrop-shapes { position: absolute; inset: 0; }

  .brand {
    position: absolute;
    display: flex;
    flex-direction: column;
    align-items: center;
  }
  .brand-row { display: flex; align-items: center; gap: 10px; }
  .brand-square { display: block; background: var(--orange); }
  .brand-name { font-weight: 700; letter-spacing: -0.5px; line-height: 1; }
  .brand-tagline { line-height: 1; }

  .card-front .brand { left: 0; right: 0; top: 88px; }
  .card-front .brand-square { width: 26px; height: 26px; }
  .card-front .brand-name { font-size: 46px; color: var(--paper); }
  .card-front .brand-tagline { font-size: 15px; color: var(--mute); margin-top: 10px; }

  .services {
    position: absolute;
    left: 0; right: 0; top: 262px;
    text-align: center;
    font-size: 12.5px;
    color: var(--mute);
  }
  .services .divider { color: var(--orange); margin: 0 5px; }

  .card-back .brand { left: 0; width: 244px; top: 146px; }
  .card-back .brand-square { width: 20px; height: 20px; }
  .card-back .brand-name { font-size: 36px; color: var(--ink); }
  .card-back .brand-tagline { font-size: 11.5px; color: var(--mute-dark); margin-top: 6px; }

  .contact-block { position: absolute; left: 292px; top: 82px; }
  .person-name {
    font-family: "Fira Sans", Arial, sans-serif;
    font-weight: 500;
    font-size: 19px;
    color: var(--orange);
  }
  .person-role { font-size: 12.5px; color: var(--paper); margin-top: 5px; }
  .contact-list { list-style: none; margin-top: 29px; }
  .contact-list li {
    display: flex;
    align-items: center;
    gap: 10px;
    height: 18.5px;
    font-size: 12.5px;
    color: var(--paper);
  }
  .contact-list svg { width: 11px; height: 11px; fill: var(--orange); flex: none; }
</style>
</head>
<body>
  <section class="card card-front">
    <div class="brand">
      <div class="brand-row">
        <span class="brand-square"></span>
        <span class="brand-name">Roomvanta</span>
      </div>
      <span class="brand-tagline">hotel pms service</span>
    </div>
    <p class="services">Hotel Software Solutions<span class="divider">|</span>Web Booking Engine<span class="divider">|</span>Multi Channel Manager</p>
  </section>

  <section class="card card-back">
    <svg class="backdrop-shapes" viewBox="0 0 482 292" preserveAspectRatio="none" aria-hidden="true">
      <rect width="482" height="292" fill="var(--charcoal)"/>
      <path d="M204 0 Q270 146 206 292 H214 Q278 146 204 0 Z" fill="var(--orange)"/>
      <path d="M0 0 H204 Q266 146 204 292 H0 Z" fill="var(--paper)"/>
    </svg>
    <div class="brand">
      <div class="brand-row">
        <span class="brand-square"></span>
        <span class="brand-name">Roomvanta</span>
      </div>
      <span class="brand-tagline">hotel pms service</span>
    </div>
    <div class="contact-block">
      <p class="person-name">Marko Vidal Lenart</p>
      <p class="person-role">Managing Director</p>
      <ul class="contact-list">
        <li>
          <svg viewBox="0 0 12 12"><path d="M1 4 Q6 0 11 4 L10 5.5 L8 4.8 V4 Q6 3 4 4 V4.8 L2 5.5 Z M3 6 H9 L10.5 10.5 H1.5 Z"/></svg>
          +38614007300
        </li>
        <li>
          <svg viewBox="0 0 12 12"><path d="M1 2.5 H11 V9.5 H1 Z M1.6 3 L6 6.6 L10.4 3 Z" fill-rule="evenodd"/></svg>
          info@roomvanta-example.net
        </li>
        <li>
          <svg viewBox="0 0 12 12"><path d="M6 1 A5 5 0 1 0 6.01 1 Z M6 2.2 Q4.4 4 4.4 6 Q4.4 8 6 9.8 Q7.6 8 7.6 6 Q7.6 4 6 2.2 Z M2.3 5.5 H9.7 V6.5 H2.3 Z" fill-rule="evenodd"/></svg>
          www.roomvanta-example.eu
        </li>
      </ul>
    </div>
  </section>
</body>
</html>
```